chocolate bar wrapper

Need a design for a new line of chocolate bars being sold at new retail candy store concept called PLINKTREATS. There will be many flavors including Dark Chocolate, Milk Chocolate, Dark Chocolate Espresso, Milk Chocolate Smores, Dark Chocolate Strawberry Champagne, Dark Chocolate Sea Salt, Dark Chocolate Chipotle, etc. Size of bar is 3 inches x 6 5/8 inches.

Please visit PLINKTREATS.EXAMPLE

Industry/Entity Type

Retail

```html
<!DOCTYPE html>
<html lang="en">
<head>
<meta charset="utf-8">
<title>Plinktreats Dark Chocolate Bar Wrapper</title>
<link rel="stylesheet" href="https://fonts.googleapis.com/css2?family=Open+Sans:wght@400;700&family=Oleo+Script&family=Arimo&display=swap">
<style>
  :root {
    --paper: #ffffff;
    --wrapper: #000000;
    --cocoa: #3d2314;
    --stripe-red: #ed1c24;
    --stripe-green: #8cc63f;
    --stripe-magenta: #ec008c;
    --stripe-cyan: #00aeef;
    --stripe-yellow: #fff200;
    --stripe-grass: #39b54a;
    --brand-pink: #e8318a;
    --ink-dark: #231f20;
    --ink-light: #ffffff;
    --ink-soft: #d6d6d6;
  }
  html, body {
    margin: 0;
    width: 1200px;
    height: 914px;
    overflow: hidden;
    background: var(--paper);
  }
  .wrapper {
    position: absolute;
    left: 407px;
    top: 5px;
    width: 450px;
    height: 987px;
    background: var(--wrapper);
    transform: scale(0.914);
    transform-origin: 0 0;
    overflow: hidden;
  }
  .wrapper-art {
    position: absolute;
    inset: 0;
    width: 450px;
    height: 987px;
  }
  .brand-name {
    position: absolute;
    left: 28px;
    top: 196px;
    margin: 0;
    font: 700 30px/1 "Open Sans", sans-serif;
    color: var(--brand-pink);
    letter-spacing: 0.5px;
  }
  .brand-tagline {
    position: absolute;
    left: 40px;
    top: 235px;
    margin: 0;
    font: 700 10px/1 "Open Sans", sans-serif;
    color: var(--ink-dark);
    letter-spacing: 0.2px;
  }
  .flavor {
    position: absolute;
    left: 247px;
    top: 271px;
    margin: 0;
    font: 400 24px/1 "Open Sans", sans-serif;
    color: var(--ink-light);
  }
  .promise {
    position: absolute;
    left: 174px;
    top: 516px;
    margin: 0;
    font: 400 18px/22px "Oleo Script", cursive;
    color: var(--ink-soft);
    letter-spacing: 1px;
  }
  .promise span { display: block; }
  .promise .first { padding-left: 13px; }
  .site {
    position: absolute;
    left: 0;
    width: 430px;
    top: 884px;
    margin: 0;
    text-align: center;
    font: 400 14px/1 "Arimo", sans-serif;
    letter-spacing: 4.5px;
    color: var(--ink-light);
  }
  .net-weight {
    position: absolute;
    left: 0;
    width: 430px;
    top: 936px;
    margin: 0;
    text-align: center;
    font: 400 12.5px/1 "Arimo", sans-serif;
    color: var(--ink-light);
  }
</style>
</head>
<body>
<main class="wrapper">
  <svg class="wrapper-art" viewBox="0 0 450 987" aria-hidden="false">
    <defs>
      <linearGradient id="truffle-tones" x1="0" y1="0" x2="1" y2="1">
        <stop offset="0" stop-color="#5a3424"/>
        <stop offset="0.5" stop-color="#7a4a33"/>
        <stop offset="1" stop-color="#3a2018"/>
      </linearGradient>
    </defs>
    <polygon class="brand-panel" points="0,177 275,177 245,260 0,260" fill="var(--paper)"/>
    <rect class="stripe" x="0" y="278" width="232" height="18" fill="var(--stripe-red)"/>
    <rect class="stripe" x="0" y="297" width="450" height="15" fill="var(--stripe-green)"/>
    <polygon class="flavor-tab" points="232,253 450,253 450,306 219,306" fill="var(--cocoa)"/>
    <rect class="stripe" x="0" y="314" width="450" height="8" fill="var(--stripe-magenta)"/>
    <rect class="stripe" x="0" y="322" width="450" height="10" fill="var(--stripe-cyan)"/>
    <polygon class="product-photo" points="215,332 450,332 450,503 168,503" fill="url(#truffle-tones)" role="img" aria-label="Photo of chocolate-covered clusters in dark paper cups"/>
    <rect class="stripe" x="0" y="342" width="450" height="9" fill="var(--stripe-yellow)"/>
    <rect class="stripe" x="0" y="351" width="450" height="13" fill="var(--stripe-grass)"/>
  </svg>

  <h1 class="brand-name">PLINKTREATS</h1>
  <p class="brand-tagline">ICE CREAM, CHOCOLATES &amp; CANDY!</p>
  <h2 class="flavor">Dark Chocolate</h2>
  <p class="promise"><span class="first">homemade finest</span><span>&amp; freshest ingredients</span></p>
  <p class="site">plinktreats.example</p>
  <p class="net-weight">NET WT 3.5OZ (100g)</p>
</main>
</body>
</html>
```